Business Card Design Project

I am community manager and social media strategist. I need a double sided business card with company logo and name. Looking for something professional, elegant but also a little bit original.

• - The logo and the colours are the company colours and a required to stay.
- The size should be: 84 x 55 mm (or 3.30 x 2.16)
- The file size should be: 1039 x 697 pixels (300 dpi)
- I'd like rounded corners. :)

Use the following contact information for the card:

Léonie Vardin
Stratégie médias sociaux / community management / édition de sites sociaux
mob. : 0687529103
leonie.vardin@postelune.fr
Twitter. : @lvardin
Skype : vardin.leonie

```html
<!DOCTYPE html>
<html lang="fr">
<head>
<meta charset="utf-8">
<title>AURELIS business card</title>
<link href="https://fonts.googleapis.com/css2?family=Open+Sans:wght@400;600;700&display=swap" rel="stylesheet">
<style>
  :root {
    --page-bg: #e9ecef;
    --brand-blue: #1769a8;
    --brand-blue-dark: #0c4d85;
    --brand-blue-light: #2a86c9;
    --ink: #3d3d3d;
    --ink-soft: #333;
    --card-white: #ffffff;
  }
  * { margin: 0; padding: 0; box-sizing: border-box; }
  html, body {
    width: 1200px; height: 846px; overflow: hidden;
    background: var(--page-bg);
    font-family: "Open Sans", Arial, sans-serif;
  }
  .sheet {
    position: relative; width: 1200px; height: 846px;
    display: flex; flex-direction: column; align-items: center; justify-content: center; gap: 44px;
  }
  .card {
    position: relative; width: 520px; height: 341px;
    border-radius: 14px; overflow: hidden;
    box-shadow: 0 4px 14px rgba(0,0,0,0.18);
  }
  /* front */
  .card-front {
    background: linear-gradient(180deg, var(--brand-blue-light) 0%, var(--brand-blue) 45%, var(--brand-blue-dark) 100%);
    display: flex; align-items: center; justify-content: center; gap: 22px;
  }
  .brand-dot {
    width: 92px; height: 92px; border-radius: 50%;
    background: var(--card-white);
  }
  .brand-name-front {
    color: var(--card-white); font-weight: 600; font-size: 62px; letter-spacing: 3px;
  }
  /* back */
  .card-back { background: var(--card-white); }
  .holder-name {
    position: absolute; left: 38px; top: 38px;
    font-size: 28px; font-weight: 700; line-height: 36px; color: var(--ink);
  }
  .holder-role {
    position: absolute; left: 38px; top: 78px; width: 430px;
    font-size: 16px; font-weight: 700; line-height: 21px; color: var(--brand-blue);
  }
  .edge-band {
    position: absolute; left: 0; top: 202px; width: 14px; height: 104px;
    background: linear-gradient(180deg, #7fb3dc 0%, var(--brand-blue) 50%, var(--brand-blue-dark) 100%);
  }
  .contact-list {
    position: absolute; left: 38px; top: 204px; list-style: none;
    font-size: 16px; color: var(--ink-soft);
  }
  .contact-list li { display: flex; align-items: center; gap: 10px; height: 25px; }
  .contact-icon { width: 14px; height: 14px; flex: none; }
  .brand-mark-back {
    position: absolute; right: 48px; bottom: 42px;
    display: flex; align-items: center; gap: 10px;
  }
  .brand-mark-back .brand-dot-small {
    width: 30px; height: 30px; border-radius: 50%; background: var(--brand-blue);
  }
  .brand-name-back {
    color: var(--brand-blue); font-weight: 600; font-size: 30px; letter-spacing: 1px;
  }
</style>
</head>
<body>
<main class="sheet">
  <section class="card card-front" aria-label="Card front">
    <span class="brand-dot"></span>
    <span class="brand-name-front">AURELIS</span>
  </section>

  <section class="card card-back" aria-label="Card back">
    <h1 class="holder-name">Léonie Vardin</h1>
    <p class="holder-role">Stratégie médias sociaux / community management / édition de sites sociaux</p>
    <div class="edge-band"></div>
    <ul class="contact-list">
      <li>
        <svg class="contact-icon" viewBox="0 0 14 14" aria-hidden="true"><rect x="3" y="1" width="8" height="12" rx="2" fill="var(--brand-blue)"/><rect x="4.5" y="3" width="5" height="5" fill="#fff"/></svg>
        0687529103
      </li>
      <li>
        <svg class="contact-icon" viewBox="0 0 14 14" aria-hidden="true"><rect x="1" y="3" width="12" height="8" fill="var(--brand-blue)"/><path d="M1 3 L7 8 L13 3" stroke="#fff" stroke-width="1.2" fill="none"/></svg>
        leonie.vardin@postelune.fr
      </li>
      <li>
        <svg class="contact-icon" viewBox="0 0 14 14" aria-hidden="true"><circle cx="7" cy="7" r="6" fill="var(--brand-blue)"/></svg>
        @lvardin
      </li>
      <li>
        <svg class="contact-icon" viewBox="0 0 14 14" aria-hidden="true"><circle cx="7" cy="7" r="6" fill="var(--brand-blue)"/></svg>
        vardin.leonie
      </li>
    </ul>
    <div class="brand-mark-back">
      <span class="brand-dot-small"></span>
      <span class="brand-name-back">AURELIS</span>
    </div>
  </section>
</main>
</body>
</html>
```